Kleine Werbebroschüre für Bauunternehmen (Deckblatt plus  1. und 2. Seite)
Kleine Werbebroschüre für Bauunternehmen (Deckblatt plus 1. und 2. Seite)
Zielgruppe
Private Bauherren, Familien
Aufgabenstellung
Guten Tag zusammen,
wir benötigen einen klein Broschüre für ein Bauunternehmen, welche angelehnt werden kann an das Design unserer Internetseite www.kolmar-steinbau.de. Die Broschüre soll nur aus einem Deckblatt und dann beim Aufklappen aus einer ersten und zweiten Seite bestehen, die Rückseite kann frei bleiben bzw. hier genügt ein kleiner farblicher Balken mit z. B. unseren Kontaktinformationen. Die Bilder, Logos und Texte, welche verarbeitet werden sollen, laden wir gerne über das Portal hoch. Zur ganz groben Orientierung haben wir ein Word Dokument angelegt und hochgeladen, das Hausbild auf dem Deckblatt muss nicht, aber kann eingebaut werden, es muss sich halt gut in das Gesamtbild einfügen. Wir wünschen uns eine modernes, hochwertiges und vertrauenserweckendes Design, die Website soll nur zur Orientierung gelten und Eure Kreativität nicht einschränken. Wir sind für alle Vorschläge offen. Wenn es fragen gibt, sind wir jederzeit für Euch ansprechbar.
Wir freuen uns auf Eure Vorschläge.
Lukas

```html
<!DOCTYPE html>
<html lang="de">
<head>
<meta charset="utf-8">
<title>Typenhäuser – Bau- und Leistungsbeschreibung</title>
<link href="https://fonts.googleapis.com/css2?family=Cabin:wght@400;500&display=swap" rel="stylesheet">
<style>
  :root {
    --band: #4d5e7e;
    --text: #4a5878;
    --page: #eef0f4;
    --panel: #dde1e8;
    --white: #ffffff;
  }
  * { margin: 0; padding: 0; box-sizing: border-box; }
  html, body { width: 848px; height: 1200px; overflow: hidden; }
  body {
    position: relative;
    background: linear-gradient(180deg, #f6f7f9 0%, var(--page) 100%);
    font-family: "Cabin", sans-serif;
    color: var(--text);
  }
  .title-band {
    position: absolute; left: 0; top: 29px; width: 848px; height: 39px;
    background: var(--band); color: var(--white);
    font-size: 25px; font-weight: 500; padding-left: 51px; line-height: 39px;
  }
  .house {
    position: absolute; width: 383px; height: 161px;
    border: 1px solid var(--band);
  }
  .house.lumio   { left: 40px;  top: 79px;  background: linear-gradient(160deg, #8fb6e2 0%, #d9e2ee 40%, #c6553a 55%, #6e8c4a 100%); }
  .house.solena  { left: 425px; top: 79px;  background: linear-gradient(160deg, #8fb6e2 0%, #c9d4dd 35%, #d99a3c 55%, #5f7f44 100%); }
  .house.verano  { left: 40px;  top: 244px; background: linear-gradient(160deg, #8fb6e2 0%, #dfe5ec 40%, #cf5a3f 52%, #f4f4f4 65%, #62803f 100%); }
  .house.altura  { left: 425px; top: 244px; background: linear-gradient(160deg, #8fb6e2 0%, #c0cad2 35%, #2e2e2e 50%, #f1ebc4 62%, #b3333a 75%, #5a7a3e 100%); }
  .house-label {
    position: absolute; right: 0; bottom: 0; width: 105px; height: 26px;
    background: var(--band); color: var(--white);
    font-size: 17.5px; text-align: center; line-height: 27px; letter-spacing: 0.3px;
  }
  .info-box {
    position: absolute; left: 23px; top: 423px; width: 801px; height: 44px;
    background: var(--band); color: var(--white);
    font-size: 12.4px; font-weight: 500; padding: 1px 0 0 5px; line-height: 20.5px;
  }
  .spec-heading {
    position: absolute; left: 25px; top: 504px;
    font-size: 18.5px; font-weight: 500;
  }
  .spec-intro {
    position: absolute; left: 26px; top: 532px; width: 800px;
    font-size: 12.2px; line-height: 15px;
  }
  .spec-panel {
    position: absolute; left: 0; top: 597px; width: 848px; height: 443px;
    background: var(--panel);
  }
  .spec-list {
    list-style: none; position: absolute; left: 0; top: 6px;
  }
  .spec-list li {
    position: relative; padding-left: 60px;
    font-size: 13px; line-height: 20.5px; height: 20.5px; white-space: nowrap;
  }
  .spec-list li::before {
    content: ""; position: absolute; left: 35px; top: 6px;
    width: 9px; height: 9px; border-radius: 50%; background: var(--band);
  }
  .closing-visual {
    position: absolute; left: 470px; top: 1040px; width: 378px; height: 131px;
    background: linear-gradient(90deg, rgba(238,240,244,1) 0%, rgba(222,200,190,0.45) 45%, rgba(200,210,195,0.6) 100%);
  }
  .footer-band {
    position: absolute; left: 0; top: 1171px; width: 848px; height: 29px;
    background: var(--band); color: var(--white);
    font-size: 13.5px; text-align: center; line-height: 29px;
  }
</style>
</head>
<body>
  <header class="title-band">Typenhäuser</header>

  <div class="house lumio" role="img" aria-label="Visualisierung Haus Lumio mit rotem Satteldach und Solarmodulen"><span class="house-label">LUMIO</span></div>
  <div class="house solena" role="img" aria-label="Visualisierung Haus Solena, zweigeschossig, orange mit Walmdach"><span class="house-label">SOLENA</span></div>
  <div class="house verano" role="img" aria-label="Visualisierung Haus Verano, weiß mit rotem Satteldach und Gaube"><span class="house-label">VERANO</span></div>
  <div class="house altura" role="img" aria-label="Visualisierung Haus Altura, cremefarben und rot mit dunklem Dach"><span class="house-label">ALTURA</span></div>

  <div class="info-box">
    Auf unserer Internetseite www.kolmar-steinbau.de finden Sie eine große Auswahl beliebten Typenhäusern.<br>
    Natürlich sind alle unsere Typenhäuser flexibel planbar bezüglich der Grundrisse und Raumaufteilung.
  </div>

  <h2 class="spec-heading">Bau- und Leistungsbeschreibung</h2>
  <p class="spec-intro">Mit der übersichtlichen Bau- und Leistungsbeschreibung, einer transparenten Kalkulation sowie einer Festpreis- und Bauzeitgarantie mit Zahlungsplan nach Baufortschritt, haben Sie immer alles genau im Blick. Die Zufriedenheit unserer Kunden steht bei uns an erster Stelle. Hier ein kurzer Überblick über die groben Eckpunkte unserer Bau- und Leistungsbeschreibung:</p>

  <section class="spec-panel">
    <ul class="spec-list">
      <li>Rohbauhöhe EG 275 cm, in allen anderen Wohngeschossen 262,5 cm</li>
      <li>Massive Außenwände aus hochdämmenden Tonwerk Lindner Hochlochziegeln Typ „Block TS9“</li>
      <li>Alle Innenwände ebenfalls massiv</li>
      <li>Dacheindeckung mit Betondachsteinen der Marke DACHSTEIN-NORD</li>
      <li>Die Regenrinnen und Regenfallrohre aus Titanzinkblech</li>
      <li>Kunststofffenster mit 5-Kammer-Profil, Wärmeschutzverglasung, Rollladen und Natursteinfensterbänken</li>
      <li>Außenputz als zweilagiger mineralischer Strukturputz + Egalisationsanstrich</li>
      <li>Gasbrennwertheizungsanlage mit Solaranlage von „Thermalis“</li>
      <li>Innenputz als einlagiger Gipsputz</li>
      <li>Dach gedämmt mit 20 cm Mineralwolle der Marke „Lanatherm“</li>
      <li>Alle Wohnräume erhalten einen Zementestrich mit Fußbodenheizung</li>
      <li>Fliesenbeläge im Wert von 25,00 € / m²</li>
      <li>Sanitärobjekte von „Keramo &amp; Sohn“ sowie Dusch- und Badewanne von „Wannhaus“ mit Armaturen von „Aquavent“</li>
      <li>Innentüren als Röhrenspansteg-Türblättern, hochwertig laminiert.</li>
      <li>Zweiholm-Stahltreppe mit Trittstufen aus Buche (stabverleimt)</li>
      <li>Bodenbeläge aus Laminat im Wert von 15,00 € / m²</li>
      <li>Wände tapeziert mit „Weimarer“ Rauhfaser</li>
      <li>sämtliche Planungs- und Bauleitungsleistungen</li>
      <li>BAUPRÜF-Bauüberwachung mit Zertifikat</li>
      <li>Festpreis-Garantie</li>
      <li>Eigenleistungen möglich</li>
    </ul>
  </section>

  <div class="closing-visual" role="img" aria-label="Verblasste Ansicht eines weißen Einfamilienhauses mit rotem Dach"></div>

  <footer class="footer-band">www.kolmar-steinbau.de</footer>
</body>
</html>
```